Fresh Tarrow Work Post - Business Card Required

Dear All,

I own Velmira Limited, which in turn owns the website:
www.harbinworkpost.example

I want all of you wonderful creative people to come up with a slick, and awesome business card design that incorporates the logo on the site, and some colouring and design elements from it.

You have free reign in how you go about doing this, I won't be giving my contact details on this platform, but the winner will be asked to redesign based on my contact details which I will supply at the end.

I need the design to be completed within 5 days. I need the final print copies of the business cards by the 25th November, so unfortunately it's a bit of a rush to get these designs ready.

Any questions, please ask.

Thank you
Updates

Thank you all for your hard work and exceptional designs provided. I do have to pick one, so I have a very clear idea of which one this is, however I will wait one further day until the competition closes to be fair to all those have submitted, or are in the process of submitting. I wish you all the best and thank you again for your dedication.

```html
<!DOCTYPE html>
<html lang="en">
<head>
<meta charset="utf-8">
<title>Fresh Tarrow Work Post – Business Card</title>
<link rel="stylesheet" href="https://fonts.googleapis.com/css2?family=Open+Sans:wght@400;600;700&display=swap">
<style>
  :root {
    --backdrop: #e9e7e3;
    --card: #3a3a3b;
    --gold-light: #f1cd72;
    --gold: #d4a23c;
    --gold-deep: #a9761f;
    --ink: #ffffff;
    --ink-soft: #ececec;
  }
  * { margin: 0; padding: 0; box-sizing: border-box; }
  html, body { width: 1200px; height: 900px; overflow: hidden; }
  body {
    background: var(--backdrop);
    font-family: "Open Sans", Arial, sans-serif;
    position: relative;
  }
  .business-card {
    position: absolute;
    left: 100px; top: 165px;
    width: 1000px; height: 570px;
    background: var(--card);
    border-radius: 56px;
    overflow: hidden;
    box-shadow: 0 14px 30px rgba(0,0,0,0.22);
  }
  .gold-swoosh { position: absolute; inset: 0; }
  .brand {
    position: absolute;
    left: 170px; top: 215px;
    width: 370px;
    display: flex; align-items: center; gap: 12px;
    white-space: nowrap;
  }
  .brand-dot {
    width: 22px; height: 22px; border-radius: 50%;
    background: var(--gold);
    flex: none;
  }
  .brand-name {
    color: var(--gold);
    font-weight: 600;
    font-size: 20px;
    letter-spacing: 1px;
    text-transform: uppercase;
  }
  .holder {
    position: absolute;
    left: 580px; top: 182px;
    color: var(--ink);
    white-space: nowrap;
  }
  .holder-name { font-weight: 700; font-size: 28px; letter-spacing: 0.5px; line-height: 36px; }
  .holder-role { font-weight: 400; font-size: 21px; line-height: 28px; color: var(--ink-soft); }
  .address {
    position: absolute;
    left: 88px; top: 320px;
    color: var(--ink);
    font-style: normal;
    font-size: 27px; line-height: 38px;
  }
  .contacts {
    position: absolute;
    left: 100px; top: 430px;
    list-style: none;
    color: var(--ink);
    font-size: 22px; line-height: 34px;
  }
  .contacts li { display: flex; align-items: center; gap: 14px; }
  .contacts svg { width: 20px; height: 20px; fill: var(--ink); flex: none; }
</style>
</head>
<body>
  <article class="business-card">
    <svg class="gold-swoosh" viewBox="0 0 1000 570" aria-hidden="true">
      <defs>
        <linearGradient id="goldFill" x1="0" y1="0" x2="1" y2="1">
          <stop offset="0" stop-color="#f1cd72"/>
          <stop offset="0.55" stop-color="#d4a23c"/>
          <stop offset="1" stop-color="#a9761f"/>
        </linearGradient>
      </defs>
      <path d="M630 0 L1000 0 L1000 570 L760 570 C900 430 910 170 630 0 Z" fill="url(#goldFill)"/>
    </svg>

    <div class="brand">
      <span class="brand-dot"></span>
      <span class="brand-name">Fresh Tarrow Work Post</span>
    </div>

    <div class="holder">
      <div class="holder-name">DORIAN HALVERS</div>
      <div class="holder-role">Managing Director</div>
    </div>

    <address class="address">
      27.14th floor,Quarry<br>Lane Road NWT
    </address>

    <ul class="contacts">
      <li>
        <svg viewBox="0 0 24 24"><path d="M6.6 10.8a15.1 15.1 0 0 0 6.6 6.6l2.2-2.2c.3-.3.7-.4 1-.2 1.1.4 2.3.6 3.6.6.6 0 1 .4 1 1V20c0 .6-.4 1-1 1A17 17 0 0 1 3 4c0-.6.4-1 1-1h3.5c.6 0 1 .4 1 1 0 1.3.2 2.5.6 3.6.1.3 0 .7-.2 1z"/></svg>
        014 228 5907
      </li>
      <li>
        <svg viewBox="0 0 24 24"><path d="M2 5h20v14H2z M4 7v.4l8 5.2 8-5.2V7z" fill-rule="evenodd"/></svg>
        hello@harbinworkpost.example
      </li>
      <li>
        <svg viewBox="0 0 24 24"><path d="M12 2a10 10 0 1 0 0 20 10 10 0 0 0 0-20zm6.9 6h-3a15 15 0 0 0-1.3-3.9A8 8 0 0 1 18.9 8zM12 4c.8 1.2 1.5 2.5 1.900 4h-3.8c.4-1.5 1.1-2.8 1.9-4zM4.3 14a8 8 0 0 1 0-4h3.4a16 16 0 0 0 0 4zm.8 2h3a15 15 0 0 0 1.3 3.9A8 8 0 0 1 5.1 16zM8.1 8h-3a8 8 0 0 1 4.3-3.9A15 15 0 0 0 8.1 8zM12 20c-.8-1.2-1.5-2.5-1.9-4h3.8c-.4 1.5-1.1 2.8-1.9 4zm2.3-6H9.7a14 14 0 0 1 0-4h4.6a14 14 0 0 1 0 4zm.3 5.9a15 15 0 0 0 1.3-3.9h3a8 8 0 0 1-4.3 3.9zM16.3 14a16 16 0 0 0 0-4h3.4a8 8 0 0 1 0 4z"/></svg>
        www.harbinworkpost.example
      </li>
    </ul>
  </article>
</body>
</html>
```